Hollisford Solar Project Sign - 36" x 48" color poster

Need a 36" x 48" sign to put next to our solar project. The solar project is installed and we will print this sign on plastic corrugated board and mount as an informational kiosk next to the project. A picture of a similar kiosk is attached. Its is important that the information is easy to understand and aesthetically pleasing. I've uploaded a draft that we did with the information and general idea. The draft is not the correct dimensions and will not scale to the appropriate size. Looking for a professional to do this well. Thank you !!
Target Market(s)
teenage school children and their parents.
Industry/Entity Type
Solar Energy
Requirements
Must have
- technical information included in the draft. Must include the photo of the solar project. Must include the Amberline Solar Logo. Must be scaled to 36" x 48".
Nice to have
- Color scheme that complements the amberline solar logo colors
Should not have
- stock photos

```html
<!DOCTYPE html>
<html lang="en">
<head>
<meta charset="utf-8">
<title>Hollisford School District Solar</title>
<link href="https://fonts.googleapis.com/css2?family=Montserrat:wght@300;400;500;800&display=swap" rel="stylesheet">
<style>
  :root{
    --navy:#0b3c77;
    --navy-light:#1a5296;
    --sky-text:#cfe3ff;
    --white:#ffffff;
    --grass-green:#4f9a3c;
    --band-dark:rgba(20,70,40,0.55);
    --orange:#f39324;
    --logo-green:#6aaa3a;
    --seal-grey:#4a4a4a;
    --bar-blue:#4472c4;
    --line-gold:#f5b400;
    --axis-grey:#595959;
    --grid-grey:#d9d9d9;
  }
  *{box-sizing:border-box;margin:0;padding:0}
  html,body{width:1200px;height:900px;overflow:hidden;background:var(--white)}
  .sign{position:relative;width:1200px;height:900px;font-family:"Montserrat",sans-serif;overflow:hidden}

  .header{position:absolute;left:0;top:0;width:1200px;height:155px;
    background:linear-gradient(115deg,var(--navy) 0%,var(--navy-light) 50%,var(--navy) 100%);
    border-bottom:3px solid var(--white);text-align:center;color:var(--white)}
  .title{font-weight:800;font-size:49px;letter-spacing:1.5px;padding-top:28px;line-height:1}
  .subtitle{font-weight:400;font-size:19.5px;color:var(--sky-text);margin-top:14px;line-height:26px}

  .site-photo{position:absolute;left:0;top:158px;width:1200px;height:742px;
    background:linear-gradient(180deg,#2d63b0 0%,#6f96cf 18%,#a9c1e0 24%,#2a3340 30%,#1d2a2c 40%,#1f3558 44%,#2c4f8c 52%,#5a5036 60%,#6b5a3a 80%,#5e4e33 100%)}

  .tint-band{position:absolute;left:0;top:656px;width:1200px;height:66px;background:var(--band-dark)}
  .green-band{position:absolute;left:0;top:722px;width:1200px;height:130px;background:rgba(79,154,60,0.93)}

  .benefits{position:absolute;left:52px;top:734px;list-style:none;color:var(--white);font-weight:400;font-size:21px;line-height:27px}
  .benefits li::before{content:"• "}

  .panel-layers{position:absolute;left:52px;top:535px;width:262px;height:169px;background:var(--white)}
  .panel-layers .layers-drawing{position:absolute;left:8px;top:10px;width:175px;height:150px;
    background:linear-gradient(160deg,#e9eef5 0%,#7f8fd6 50%,#d8dde4 100%)}
  .panel-layers .layer-label{position:absolute;left:197px;font-size:7.5px;color:#444;line-height:1}
  .panel-layers .layer-label::before{content:"";position:absolute;left:-16px;top:4px;width:12px;border-top:1px solid #999}

  .energy-chart{position:absolute;left:329px;top:535px;width:279px;height:169px;background:var(--white)}

  .logo-card{position:absolute;left:688px;top:722px;width:481px;height:130px;background:var(--white);border-top:7px solid var(--orange)}
  .seal{position:absolute;left:27px;top:38px;width:60px;height:60px;border-radius:50%;background:var(--seal-grey)}
  .brand-name{position:absolute;left:110px;top:42px;font-weight:800;font-size:38px;letter-spacing:1px;color:var(--logo-green);line-height:1}

  .completion{position:absolute;right:31px;top:866px;color:var(--white);font-weight:500;font-size:19.5px}
</style>
</head>
<body>
<div class="sign">
  <header class="header">
    <h1 class="title">HOLLISFORD SCHOOL DISTRICT SOLAR</h1>
    <p class="subtitle">Incentives from Vermont’s net metering program, renewable energy credits and<br>energy savings pay for this project without adding cost to the district or tax payers</p>
  </header>

  <div class="site-photo" role="img" aria-label="Photo of the ground-mounted solar array in a grassy field in front of a tree line under a blue sky"></div>
  <div class="tint-band"></div>
  <div class="green-band"></div>

  <div class="panel-layers">
    <div class="layers-drawing" role="img" aria-label="Exploded view of a solar module showing its stacked layers"></div>
    <span class="layer-label" style="top:31px">Frame</span>
    <span class="layer-label" style="top:53px">Glass</span>
    <span class="layer-label" style="top:73px">Encapsulant</span>
    <span class="layer-label" style="top:90px">Solar Cells</span>
    <span class="layer-label" style="top:109px">Encapsulant</span>
    <span class="layer-label" style="top:127px">Backsheet</span>
    <span class="layer-label" style="top:146px">Junction Box</span>
  </div>

  <svg class="energy-chart" viewBox="0 0 279 169" aria-label="Monthly expected energy and global horizontal irradiance">
    <g stroke="var(--grid-grey)" stroke-width="0.6">
      <line x1="55" x2="232" y1="111" y2="111"/><line x1="55" x2="232" y1="100.8" y2="100.8"/>
      <line x1="55" x2="232" y1="90.6" y2="90.6"/><line x1="55" x2="232" y1="80.4" y2="80.4"/>
      <line x1="55" x2="232" y1="70.2" y2="70.2"/><line x1="55" x2="232" y1="60" y2="60"/>
      <line x1="55" x2="232" y1="49.8" y2="49.8"/><line x1="55" x2="232" y1="39.6" y2="39.6"/>
      <line x1="55" x2="232" y1="29.4" y2="29.4"/><line x1="55" x2="232" y1="19.2" y2="19.2"/>
      <line x1="55" x2="232" y1="9" y2="9"/>
    </g>
    <g font-family="Montserrat, sans-serif" font-size="6.5" fill="var(--axis-grey)" text-anchor="end">
      <text x="52" y="113">0</text><text x="52" y="102.8">20</text><text x="52" y="92.6">40</text>
      <text x="52" y="82.4">60</text><text x="52" y="72.2">80</text><text x="52" y="62">100</text>
      <text x="52" y="51.8">120</text><text x="52" y="41.6">140</text><text x="52" y="31.4">160</text>
      <text x="52" y="21.2">180</text><text x="52" y="11">200</text>
    </g>
    <g font-family="Montserrat, sans-serif" font-size="6.5" fill="var(--axis-grey)">
      <text x="238" y="113">0</text><text x="238" y="98.4">5000</text><text x="238" y="83.8">10000</text>
      <text x="238" y="69.3">15000</text><text x="238" y="54.7">20000</text><text x="238" y="40.2">25000</text>
      <text x="238" y="25.6">30000</text><text x="238" y="11">35000</text>
    </g>
    <text transform="translate(15,108) rotate(-90)" font-family="Montserrat, sans-serif" font-size="6.5" fill="var(--axis-grey)">Global Horizontal Irradiance</text>
    <text transform="translate(24,95) rotate(-90)" font-family="Montserrat, sans-serif" font-size="6.5" fill="var(--axis-grey)">(kWh/m²)</text>
    <text transform="translate(270,82) rotate(-90)" font-family="Montserrat, sans-serif" font-size="6.5" fill="var(--axis-grey)">Expected Energy (kWh)</text>
    <g fill="var(--bar-blue)">
      <rect x="60.3" y="68.7" width="4" height="42.3"/><rect x="74.9" y="62" width="4" height="49"/>
      <rect x="89.5" y="57.1" width="4" height="53.9"/><rect x="104.1" y="52.7" width="4" height="58.3"/>
      <rect x="118.6" y="36.7" width="4" height="74.3"/><rect x="133.2" y="42.5" width="4" height="68.5"/>
      <rect x="147.8" y="28.8" width="4" height="82.2"/><rect x="162.4" y="21.2" width="4" height="89.8"/>
      <rect x="177" y="46.9" width="4" height="64.1"/><rect x="191.5" y="65.8" width="4" height="45.2"/>
      <rect x="206.1" y="76.6" width="4" height="34.4"/><rect x="220.7" y="86.2" width="4" height="24.8"/>
    </g>
    <polyline fill="none" stroke="var(--line-gold)" stroke-width="1.2"
      points="62.3,86.5 76.9,77.9 91.5,65.1 106.1,52.4 120.6,35.5 135.2,39.6 149.8,25.3 164.4,24.3 179,49.8 193.5,77.9 208.1,90.6 222.7,95.7"/>
    <g font-family="Montserrat, sans-serif" font-size="6.5" fill="var(--axis-grey)" text-anchor="end">
      <text transform="translate(65,118) rotate(-45)">January</text>
      <text transform="translate(79.6,118) rotate(-45)">February</text>
      <text transform="translate(94.2,118) rotate(-45)">March</text>
      <text transform="translate(108.8,118) rotate(-45)">April</text>
      <text transform="translate(123.3,118) rotate(-45)">May</text>
      <text transform="translate(137.9,118) rotate(-45)">June</text>
      <text transform="translate(152.5,118) rotate(-45)">July</text>
      <text transform="translate(167.1,118) rotate(-45)">August</text>
      <text transform="translate(181.7,118) rotate(-45)">September</text>
      <text transform="translate(196.2,118) rotate(-45)">October</text>
      <text transform="translate(210.8,118) rotate(-45)">November</text>
      <text transform="translate(225.4,118) rotate(-45)">December</text>
    </g>
    <rect x="48" y="154" width="10" height="4" fill="var(--bar-blue)"/>
    <text x="60" y="158.5" font-family="Montserrat, sans-serif" font-size="6.5" fill="var(--axis-grey)">Expected Energy</text>
    <line x1="128" x2="140" y1="156" y2="156" stroke="var(--line-gold)" stroke-width="1.2"/>
    <text x="142" y="158.5" font-family="Montserrat, sans-serif" font-size="6.5" fill="var(--axis-grey)">Global Horizontal Irradiance</text>
  </svg>

  <ul class="benefits">
    <li>Project provides energy savings to school district</li>
    <li>New powerline provides electricity to snack shack</li>
    <li>Provides curriculum opportunity for students</li>
    <li>Solar energy generated without burning fossil</li>
  </ul>

  <div class="logo-card">
    <div class="seal"></div>
    <div class="brand-name">AMBERLINE SOLAR</div>
  </div>

  <p class="completion">Project Completed on December 2015</p>
</div>
</body>
</html>
```